Family owned plumbing contractor needs eye catching business card design

Business cards that are unique, eye catching, and provide customers with general company information, such as name, address, phone number, website, employee name/title, cell phone #, & email address. We are transitioning to a new logo that utilizes a more retro feel, so we are interested in seeing some cool old school designs in the mix. We are liking the dark background on some of the samples on this website. If that is workable with our artwork, we would like to see that incorporated into the design.
Contact Information for Business Card
Copperline Pipeworks, Inc.
www.copperlinepipeworks.example
(555) 392-7068 phone
Nevada License #64205
California License #5810473
Dale Wrennick, President
(555) 618-9032 cell
dale@copperlinepipeworks.example
Residential * Commercial * Service
Requirements
Must have
- The business card details listed above & logo provided.
Nice to have
- I made some notes about color options in the description.

```html
<!DOCTYPE html>
<html lang="en">
<head>
<meta charset="utf-8">
<title>Copperline Pipeworks – Business Card</title>
<link href="https://fonts.googleapis.com/css2?family=Lobster+Two:ital@1&family=Tinos&display=swap" rel="stylesheet">
<style>
  :root {
    --backdrop: #d9d9d9;
    --card-white: #f7f7f5;
    --card-teal: #7ccdbf;
    --texture-teal: #a9ddd3;
    --ink-slate: #3f6384;
    --ink-teal: #5fb3a6;
    --ink-grey: #4a4a4a;
  }
  * { margin: 0; padding: 0; box-sizing: border-box; }
  html, body {
    width: 1200px;
    height: 800px;
    overflow: hidden;
    background: var(--backdrop);
  }
  .stage {
    position: relative;
    width: 1200px;
    height: 800px;
  }
  .card {
    position: absolute;
    top: 255px;
    width: 500px;
    height: 286px;
    box-shadow: 0 2px 6px rgba(0,0,0,0.18);
  }
  .card--front {
    left: 70px;
    background: var(--card-white);
  }
  .card--back {
    left: 630px;
    background: var(--card-teal);
    overflow: hidden;
  }
  .holder {
    position: absolute;
    top: 24px;
    right: 30px;
    text-align: right;
    font-family: "Lobster Two", cursive;
    font-style: italic;
  }
  .holder__name {
    font-size: 28px;
    color: var(--ink-slate);
    line-height: 1;
  }
  .holder__title {
    font-size: 17px;
    color: var(--ink-teal);
    line-height: 1.1;
    margin-right: 2px;
  }
  .contact {
    position: absolute;
    left: 30px;
    bottom: 24px;
    font-family: "Tinos", serif;
    font-size: 13px;
    line-height: 1.3;
    color: var(--ink-grey);
    list-style: none;
  }
  .contact__gap { margin-top: 6px; }
  .texture {
    position: absolute;
    inset: 0;
    background: radial-gradient(ellipse at 40% 40%, var(--texture-teal) 0%, var(--card-teal) 70%);
    opacity: 0.55;
  }
  .brand {
    position: absolute;
    left: 0;
    right: 0;
    top: 118px;
    text-align: center;
    font-family: "Tinos", serif;
    font-size: 26px;
    color: var(--ink-slate);
  }
  .tagline {
    position: absolute;
    right: 22px;
    bottom: 18px;
    font-family: "Tinos", serif;
    font-size: 9px;
    letter-spacing: 0.08em;
    text-transform: uppercase;
    color: var(--ink-slate);
  }
</style>
</head>
<body>
<main class="stage">
  <section class="card card--front">
    <div class="holder">
      <p class="holder__name">Dale Wrennick</p>
      <p class="holder__title">President</p>
    </div>
    <ul class="contact">
      <li>Copperline Pipeworks, Inc</li>
      <li>California License #5810473</li>
      <li>Nevada License #64205</li>
      <li class="contact__gap">P. (555) 392-7068</li>
      <li>M. (555) 618-9032</li>
      <li>dale@copperlinepipeworks.example</li>
      <li>www.copperlinepipeworks.example</li>
    </ul>
  </section>

  <section class="card card--back">
    <div class="texture" role="img" aria-label="Distressed crackle texture in pale teal"></div>
    <p class="brand">Copperline Pipeworks, Inc.</p>
    <p class="tagline">Residential &#10022; Commercial &#10022; Service</p>
  </section>
</main>
</body>
</html>
```